pharmacy/travel clinic business card design

We need a business card for our new business called Merrow Travel Clinic and Pharmacy. Our primary focus is doing consultations for people before travelling internationally and providing vaccinations and prescriptions for them. While the business is considered a pharmacy, it has more the look and feel of a doctor's office. The design should communicate a professional and trustworthy feel. I have attached a copy of the logo we are going to be using.
Updates
Thanks for the submissions.  If you haven`t been eliminated you are one of the finalists.  Decision will likely be made tomorrow.

Target Market(s)
Customers, other health care professionals, travel agents
Industry/Entity Type
Clinic
Look and feel
Each slider illustrates characteristics of the customer's brand and the style your logo design should communicate.

```html
<!DOCTYPE html>
<html lang="en">
<head>
<meta charset="utf-8">
<title>Merrow Travel Clinic and Pharmacy — Business Card</title>
<link rel="stylesheet" href="https://fonts.googleapis.com/css2?family=Source+Sans+3:wght@400;600&display=swap">
<style>
  :root {
    --page-bg: #2b2b2b;
    --front-top: #3aaee3;
    --front-mid: #2a7fcb;
    --front-bottom: #0e3889;
    --card-white: #ffffff;
    --brand-blue: #1f9ad8;
    --navy: #163e8e;
    --text-dark: #333333;
    --icon-blue: #1f9ad8;
  }
  * { box-sizing: border-box; margin: 0; padding: 0; }
  html, body {
    width: 1200px; height: 900px; overflow: hidden;
    background: var(--page-bg);
    font-family: "Source Sans 3", Arial, sans-serif;
  }
  .canvas { position: relative; width: 1200px; height: 900px; }
  .card {
    position: absolute; top: 308px;
    width: 513px; height: 283px;
    border-radius: 18px; overflow: hidden;
  }
  .card--front {
    left: 72px;
    background: linear-gradient(180deg, var(--front-top) 0%, var(--front-mid) 50%, var(--front-bottom) 100%);
  }
  .card--back { left: 615px; background: var(--card-white); }

  .wordmark {
    position: absolute; transform: translate(-50%, -50%);
    font-weight: 600; line-height: 0.95; text-align: left; white-space: nowrap;
  }
  .wordmark span { display: block; }
  .card--front .wordmark { left: 256px; top: 142px; color: #ffffff; }
  .card--front .wordmark .wm-line1 { font-size: 34px; }
  .card--front .wordmark .wm-line2 { font-size: 36px; letter-spacing: -0.5px; }
  .card--front .wordmark .wm-line3 { font-size: 15px; margin-top: 3px; }

  .card--back .wordmark { left: 130px; top: 142px; color: var(--brand-blue); }
  .card--back .wordmark .wm-line1 { font-size: 25px; }
  .card--back .wordmark .wm-line2 { font-size: 27px; letter-spacing: -0.4px; }
  .card--back .wordmark .wm-line3 { font-size: 12px; margin-top: 2px; }

  .divider {
    position: absolute; left: 257px; top: 43px;
    width: 2px; height: 196px;
    background: linear-gradient(180deg, var(--brand-blue), var(--navy));
  }
  .contact { position: absolute; right: 28px; top: 44px; text-align: right; }
  .person-name { font-size: 21px; font-weight: 400; color: var(--brand-blue); line-height: 1.1; }
  .person-title { font-size: 13px; color: var(--text-dark); margin-top: 5px; }
  .details { list-style: none; margin-top: 20px; }
  .details li {
    display: flex; justify-content: flex-end; align-items: center;
    font-size: 12px; color: var(--text-dark); height: 16px;
  }
  .details li.gap { margin-top: 14px; }
  .details svg { width: 10px; height: 10px; margin-left: 6px; fill: var(--icon-blue); flex: none; }
  .details .no-icon::after { content: ""; display: inline-block; width: 16px; }
</style>
</head>
<body>
<main class="canvas">
  <section class="card card--front" aria-label="Card front">
    <div class="wordmark">
      <span class="wm-line1">Merrow</span>
      <span class="wm-line2">Travel Clinic</span>
      <span class="wm-line3">and PHARMACY</span>
    </div>
  </section>

  <section class="card card--back" aria-label="Card back">
    <div class="wordmark">
      <span class="wm-line1">Merrow</span>
      <span class="wm-line2">Travel Clinic</span>
      <span class="wm-line3">and PHARMACY</span>
    </div>
    <div class="divider"></div>
    <div class="contact">
      <p class="person-name">Daniel Hartley</p>
      <p class="person-title">managing director</p>
      <ul class="details">
        <li>555 201 4410
          <svg viewBox="0 0 10 10"><path d="M2.5 0h5a1 1 0 0 1 1 1v8a1 1 0 0 1-1 1h-5a1 1 0 0 1-1-1V1a1 1 0 0 1 1-1zm.5 1.5v6h4v-6z"/></svg></li>
        <li>info@merrowtravel.com
          <svg viewBox="0 0 10 10"><path d="M0 2h10v.8L5 5.8 0 2.8zM0 3.9l5 3 5-3V8H0z"/></svg></li>
        <li class="gap">48 Harbor Lane
          <svg viewBox="0 0 10 10"><path d="M5 0a3.5 3.5 0 0 1 3.5 3.5C8.5 6 5 10 5 10S1.5 6 1.5 3.5A3.5 3.5 0 0 1 5 0zm0 2a1.5 1.5 0 1 0 0 3 1.5 1.5 0 0 0 0-3z"/></svg></li>
        <li class="no-icon">Millbrook, New York 12545</li>
        <li>555 201 4420
          <svg viewBox="0 0 10 10"><path d="M5 0a5 5 0 1 1 0 10A5 5 0 0 1 5 0zm-1.6 2.4L2.6 3.2c.4 2 2 3.7 4.2 4.2l.8-.8-1.2-1-.6.5c-.8-.4-1.5-1.1-1.9-1.9l.5-.6z"/></svg></li>
        <li>555 201 4430
          <svg viewBox="0 0 10 10"><path d="M2.5 0h5v2.5h-5zM0 3h10v4.5H8V6H2v1.5H0zm2.5 4h5v3h-5z"/></svg></li>
        <li>www.merrowtravel.com
          <svg viewBox="0 0 10 10"><path d="M5 0a5 5 0 1 1 0 10A5 5 0 0 1 5 0zM1.1 4.4h1.9c0-1.2.3-2.3.7-3.1A4 4 0 0 0 1.1 4.4zm2.9 0h2c0-1.3-.4-2.5-1-3.3-.6.8-1 2-1 3.3zm3 0h1.9A4 4 0 0 0 6.3 1.3c.4.8.7 1.9.7 3.1zM1.1 5.6a4 4 0 0 0 2.6 3.1c-.4-.8-.7-1.9-.7-3.1zm2.9 0c0 1.3.4 2.5 1 3.3.6-.8 1-2 1-3.3zm3 0c0 1.2-.3 2.3-.7 3.1a4 4 0 0 0 2.6-3.1z"/></svg></li>
      </ul>
    </div>
  </section>
</main>
</body>
</html>
```